Premium Corporate Website Design for Velmora Systems

Our company Velmora Systems GmbH (formerly BrightHarbor GmbH) is looking for a new, modern, and professional corporate website. The content should be based on our existing site bright-harbor.example
, but reimagined in a contemporary, tech-oriented, and premium design.

Requirements:

- Alignment with the new Velmora Systems logo and corporate identity
- Modern layout that reflects the tech and IT consulting industry
- Clear and user-friendly structure with intuitive navigation
- Premium look and feel that highlights our market position
- Incorporation of animated or interactive elements to add dynamism
- Design should clearly stand out from competitors such as Durlak GmbH, TMPulse, Vorndal, Marvix, and Holtreuven
- International focus: Since our company also operates in the U.S. market, the website should reflect a global presence (e.g., bilingual structure in German/English, international visual language, U.S.-inspired corporate design elements)

Goal:
To create a high-quality, innovative, and brand-strong website that positions Velmora Systems GmbH as a modern, trustworthy, and future-oriented IT consulting company — both in the German-speaking region and in the United States.

In addition to the design, we would also like the website to be delivered as functional HTML/CSS files (or WordPress implementation if possible).

All images from our current website www.bright-harbor.example
can be used if needed. Designers are welcome to reuse or adapt this material where appropriate."

Target Market(s)

Medium to large enterprises in the technology, finance, and energy sectors Companies seeking premium IT consulting, quality assurance, and test automation services Decision makers and executives (CIOs, CTOs, IT managers) in Europe and the United States A global audience that values innovation, professionalism, and trust

Industry/Entity Type

Information Technology & Consulting Software Testing & Quality Assurance Technology / Professional Services

Coding

Number of Pages Required

Requirements
Must have
• - Integration of the Velmora Systems logo and corporate identity - Bilingual setup (German & English) Modern, premium tech design with a professional look and feel Clear structure and intuitive navigation for easy usability Responsive design, optimized for desktop, tablet, and mobile High-quality visuals and dynamic elements (animations, interactive features) Strong differentiation from competitors (Durlak GmbH, TMPulse, Vorndal, Marvix, Holtreuven)
Nice to have
• Subtle micro-animations and hover effects to enhance user experience Custom icons or illustrations that align with the Velmora brand Dark/Light mode toggle for modern usability Blog or insights section to share expertise and updates SEO-friendly structure for better visibility in search engines Integration of social media feeds (LinkedIn, Facebook, Instagram) Contact form with automation (e.g., PHPMailer or CRM integration) Showcasing case studies or success stories with an engaging layout
Should not have
• Overly crowded or cluttered layouts Stock images that look generic or low quality Outdated design styles (e.g., gradients from the 2000s, heavy drop shadows) Complex navigation that confuses users Excessive use of bright or non-brand colors outside the Velmora identity Long loading times caused by oversized media files Pop-ups or intrusive ads that disrupt the premium brand image

```html
<!DOCTYPE html>
<html lang="en">
<head>
<meta charset="utf-8">
<title>Velmora Systems GmbH – IT Consulting &amp; Quality Assurance</title>
<link href="https://fonts.googleapis.com/css2?family=Inter:wght@400;500;600;700&display=swap" rel="stylesheet">
<style>
:root{
  --bg:#000405;
  --ink:#ffffff;
  --muted:#d4dcdc;
  --card:#04181a;
  --card-edge:#0a2a2b;
  --line:#2b3a3a;
  --teal:#0e5a5c;
  --green:#1f8a45;
  --blue:#1a5fe0;
  --lime:#3bd45a;
  --link:#2f7ff0;
  --btn-grad:linear-gradient(90deg,var(--blue),var(--lime));
}
*{box-sizing:border-box;margin:0;padding:0}
html,body{width:1200px;height:3188px;overflow:hidden}
body{
  position:relative;background:var(--bg);color:var(--ink);
  font-family:"Inter",Arial,sans-serif;
}
.glow{position:absolute;pointer-events:none}
.abs{position:absolute}

/* background atmosphere */
.hero-bg{left:0;top:0;width:1200px;height:640px;
  background:
   radial-gradient(ellipse 160px 360px at 0 300px,rgba(30,170,110,.75),transparent 70%),
   radial-gradient(ellipse 160px 360px at 1200px 300px,rgba(30,170,110,.75),transparent 70%),
   radial-gradient(ellipse 700px 260px at 600px 520px,rgba(20,120,70,.55),transparent 70%);}
.hero-ring{left:330px;top:70px;width:540px;height:520px;border-radius:50%;
  background:radial-gradient(circle,rgba(0,0,0,0) 52%,rgba(90,60,140,.35) 60%,rgba(60,150,80,.5) 68%,rgba(0,0,0,0) 76%);
  filter:blur(14px)}
.who-bg{left:0;top:640px;width:1200px;height:520px;
  background:radial-gradient(ellipse 650px 260px at 600px 450px,rgba(15,110,80,.45),transparent 70%),
             radial-gradient(ellipse 500px 200px at 600px 120px,rgba(10,80,90,.35),transparent 70%)}
.svc-bg{left:0;top:1180px;width:1200px;height:440px;
  background:radial-gradient(ellipse 680px 230px at 600px 400px,rgba(20,120,60,.55),transparent 70%)}
.stories-bg{left:0;top:1620px;width:1200px;height:630px;
  background:radial-gradient(ellipse 700px 260px at 600px 500px,rgba(10,90,80,.5),transparent 70%),
             radial-gradient(ellipse 500px 200px at 600px 30px,rgba(10,70,90,.35),transparent 70%)}
.contact-bg{left:0;top:2471px;width:1200px;height:717px;
  background:radial-gradient(ellipse 420px 220px at 600px 80px,rgba(10,80,100,.5),transparent 70%),
             radial-gradient(ellipse 650px 200px at 600px 560px,rgba(20,110,60,.5),transparent 70%)}

/* nav */
.nav{left:0;width:1200px;height:60px}
.brand{position:absolute;left:105px;display:flex;align-items:center;gap:10px;
  font-weight:600;font-size:15px;color:var(--ink)}
.brand-dot{width:24px;height:24px;border-radius:50%;background:#24b06a}
.nav-links{position:absolute;top:0;left:0;list-style:none}
.nav-links li{position:absolute;font-size:11px;white-space:nowrap}
.caret{font-size:7px;color:var(--lime);margin-left:2px}
.btn{position:absolute;display:flex;align-items:center;justify-content:center;
  height:28px;border-radius:14px;font-size:11px;color:var(--ink)}
.btn-outline{border:1px solid #1f9a7a;background:rgba(0,0,0,.3)}
.btn-fill{background:var(--btn-grad)}

/* hero */
.hero-title{left:0;width:1200px;top:208px;text-align:center;font-weight:600;
  font-size:75px;line-height:86px;letter-spacing:.5px}
.hero-sub{left:0;width:1200px;top:402px;text-align:center;font-size:12.5px;line-height:19px;color:var(--muted)}

.rule{left:99px;width:1002px;height:1px;background:var(--line)}

.h2{left:0;width:1200px;text-align:center;font-weight:600;font-size:32px}
.lead{left:320px;width:560px;text-align:center;font-size:12.5px;line-height:19px;color:var(--muted)}

/* feature cards */
.card{position:absolute;width:234px;border-radius:8px;
  background:linear-gradient(180deg,#031214,#041a1b);border:1px solid var(--card-edge)}
.feat{top:810px;height:263px;text-align:center}
.feat-icon{position:absolute;left:75px;top:30px;width:84px;height:84px;border-radius:50%;
  background:linear-gradient(180deg,#1670a8,#0f4a3a);display:flex;align-items:center;justify-content:center}
.card-title{position:absolute;left:0;width:100%;text-align:center;font-weight:600;font-size:16px}
.card-text{position:absolute;left:20px;width:194px;text-align:center;font-size:12.5px;line-height:19px;color:var(--muted)}

/* service cards */
.svc{top:1278px;height:264px}
.svc-img{position:absolute;left:0;top:0;width:100%;height:126px;border-radius:8px 8px 0 0}
.svc-go{position:absolute;left:96px;top:240px;width:42px;height:42px;border-radius:50%;
  background:#021010;border:1px solid #2fae5c;display:flex;align-items:center;justify-content:center;
  color:#4ac070;font-size:12px}

/* stories */
.arrow-btn{position:absolute;top:1656px;width:43px;height:43px;border-radius:50%;
  border:1px solid #1d5fd0;display:flex;align-items:center;justify-content:center;color:#3ccf6a;font-size:14px}
.story{position:absolute;top:1776px;width:438px}
.story-img{height:195px;border-radius:6px}
.story h3{margin-top:26px;font-weight:500;font-size:34px;line-height:42px}
.story p{font-size:12.5px;line-height:19px;color:var(--muted);margin-top:10px}
.story p + p{margin-top:19px}
.story a{display:block;margin-top:9px;font-size:12.5px;color:var(--link);text-decoration:none}

/* cta band */
.cta{left:0;top:2246px;width:1200px;height:225px;
  background:linear-gradient(100deg,#3a7a3e 0%,#2a6a36 40%,#3e8a46 75%,#2a6a3a 100%)}
.cta-title{left:0;width:1200px;top:2318px;text-align:center;font-weight:600;font-size:32px}

/* contact form */
.field{position:absolute;left:99px;width:394px;border-bottom:1px solid #8a9a9a;
  font-size:12.5px;padding-bottom:14px}
.contact-img{left:543px;top:2640px;width:557px;height:315px;border-radius:6px;
  background:radial-gradient(ellipse at 50% 40%,#2d5a80,#163a5a 60%,#0f2c45)}

.footer-line{left:22px;width:1156px;height:1px;background:#2a3333}
.copy{left:0;width:1200px;top:3158px;text-align:center;font-size:11px;color:var(--muted)}
</style>
</head>
<body>

<div class="glow hero-bg"></div>
<div class="glow hero-ring"></div>
<div class="glow who-bg"></div>
<div class="glow svc-bg"></div>
<div class="glow stories-bg"></div>
<div class="glow contact-bg"></div>

<!-- header -->
<header class="abs nav" style="top:15px">
  <div class="brand" style="top:17px"><span class="brand-dot"></span>Velmora Systems GmbH</div>
  <ul class="nav-links">
    <li style="left:376px;top:23px">Home</li>
    <li style="left:465px;top:23px">About</li>
    <li style="left:556px;top:23px">Services<span class="caret">▾</span></li>
    <li style="left:658px;top:23px">Case Studies<span class="caret">▾</span></li>
    <li style="left:784px;top:23px">Contact</li>
  </ul>
  <a class="btn btn-outline" style="left:970px;top:16px;width:130px">Get Started</a>
</header>

<!-- hero -->
<h1 class="abs hero-title">IT Consulting &amp; Quality<br>Assurance</h1>
<p class="abs hero-sub">Velmora empowers businesses across Europe and the U.S. with innovative IT strategies and<br>meticulous quality assurance, driving efficiency and excellence.</p>
<a class="btn btn-outline" style="left:461px;top:458px;width:131px">Get Started</a>
<a class="btn btn-fill" style="left:606px;top:458px;width:131px">Contact Us</a>

<div class="abs rule" style="top:622px"></div>

<!-- who we are -->
<h2 class="abs h2" style="top:662px">Who We Are</h2>
<p class="abs lead" style="top:708px">Velmora is a leading IT consulting and quality assurance firm dedicated to empowering businesses with robust technology solutions and unwavering quality standards. We bridge the gap between innovation and reliability, ensuring your digital journey is seamless and successful.</p>

<div class="card feat" style="left:99px">
  <div class="feat-icon"><svg width="30" height="30" viewBox="0 0 24 24" fill="none" stroke="#fff" stroke-width="1.3"><circle cx="12" cy="12" r="9"/><ellipse cx="12" cy="12" rx="4" ry="9"/><path d="M3 12h18M4.5 7.5h15M4.5 16.5h15"/></svg></div>
  <div class="card-title" style="top:136px">Global Presence</div>
  <p class="card-text" style="top:172px">Empowering businesses across Europe and the U.S. with our strategic locations.</p>
</div>
<div class="card feat" style="left:355px">
  <div class="feat-icon"><svg width="30" height="30" viewBox="0 0 24 24" fill="none" stroke="#fff" stroke-width="1.3"><circle cx="12" cy="11" r="3"/><path d="M12 4v2M12 16v2M5 11h2M17 11h2M7 6l1.5 1.5M15.5 14.5L17 16M17 6l-1.5 1.5M8.5 14.5L7 16"/><path d="M9 19h6M10 21h4"/></svg></div>
  <div class="card-title" style="top:136px">Innovative IT Solutions</div>
  <p class="card-text" style="top:172px">Empowering businesses across Europe and the U.S. with our strategic locations.</p>
</div>
<div class="card feat" style="left:611px">
  <div class="feat-icon"><svg width="32" height="32" viewBox="0 0 24 24" fill="none" stroke="#fff" stroke-width="1.3"><circle cx="12" cy="9" r="2.6"/><circle cx="6" cy="10" r="2"/><circle cx="18" cy="10" r="2"/><path d="M7.5 17c0-2.5 2-4 4.5-4s4.5 1.5 4.5 4z"/><path d="M2.5 16c0-2 1.5-3 3.5-3M21.5 16c0-2-1.5-3-3.5-3"/></svg></div>
  <div class="card-title" style="top:136px">Trusted by Enterprises</div>
  <p class="card-text" style="top:172px">Empowering businesses across Europe and the U.S. with our strategic locations.</p>
</div>
<div class="card feat" style="left:867px">
  <div class="feat-icon"><svg width="30" height="30" viewBox="0 0 24 24" fill="none" stroke="#fff" stroke-width="1.3"><circle cx="13" cy="7" r="3.5"/><path d="M11.5 10.5l-.5 3 2-1 2 1-.5-3"/><path d="M3 16l3-1.5c1-.5 2-.5 3 0l3 1h3c1 0 1 1.5 0 1.5h-4M6 20l2-1h6l6-4"/></svg></div>
  <div class="card-title" style="top:136px">Quality Assurance</div>
  <p class="card-text" style="top:172px">Empowering businesses across Europe and the U.S. with our strategic locations.</p>
</div>

<div class="abs rule" style="top:1152px"></div>

<!-- services -->
<div class="card svc" style="left:99px">
  <div class="svc-img" role="img" aria-label="Consultants meeting at a desk with laptops" style="background:linear-gradient(135deg,#8a8a86,#4a4844 55%,#2a2826)"></div>
  <div class="card-title" style="top:146px">IT Consulting</div>
  <p class="card-text" style="top:174px">Empowering businesses across Europe and the U.S. with our strategic locations.</p>
  <div class="svc-go">↗</div>
</div>
<div class="card svc" style="left:355px">
  <div class="svc-img" role="img" aria-label="Hands typing on a laptop running automated tests" style="background:linear-gradient(135deg,#c8ccd0,#5a6a78 50%,#2a3440)"></div>
  <div class="card-title" style="top:146px">Test Automation</div>
  <p class="card-text" style="top:174px">Empowering businesses across Europe and the U.S. with our strategic locations.</p>
  <div class="svc-go">↗</div>
</div>
<div class="card svc" style="left:611px">
  <div class="svc-img" role="img" aria-label="Developers reviewing code on monitors" style="background:linear-gradient(135deg,#5a3a30,#2a2a2e 50%,#6a6a78)"></div>
  <div class="card-title" style="top:146px">Software Testing</div>
  <p class="card-text" style="top:174px">Empowering businesses across Europe and the U.S. with our strategic locations.</p>
  <div class="svc-go">↗</div>
</div>
<div class="card svc" style="left:867px">
  <div class="svc-img" role="img" aria-label="Business person holding a glowing shield with a check mark" style="background:radial-gradient(ellipse at 50% 40%,#3a6a90,#173a5c 60%,#0e2a42)"></div>
  <div class="card-title" style="top:146px">Quality Assurance</div>
  <p class="card-text" style="top:174px">Empowering businesses across Europe and the U.S. with our strategic locations.</p>
  <div class="svc-go">↗</div>
</div>

<div class="abs rule" style="top:1609px"></div>

<!-- client stories -->
<h2 class="abs h2" style="top:1656px;font-size:34px">Client Success Stories</h2>
<div class="arrow-btn" style="left:998px">←</div>
<div class="arrow-btn" style="left:1057px">→</div>

<article class="story" style="left:99px">
  <div class="story-img" role="img" aria-label="Overhead view of a team working around a table with tablets" style="background:linear-gradient(135deg,#2a3034,#1a1c1e 50%,#3a3230)"></div>
  <h3>Challenge &amp; Solution</h3>
  <p>A global logistics firm faced challenges with manual data entry and fragmented legacy systems, leading to inefficiencies and human errors.</p>
  <p>Velmora implemented an AI-driven automation platform, integrating disparate systems and streamlining data workflows, reducing operational costs by 30%.</p>
  <a href="#">Read Case Study.....</a>
</article>
<article class="story" style="left:663px">
  <div class="story-img" role="img" aria-label="Colleagues in discussion in a modern office" style="background:linear-gradient(135deg,#2a3a5a,#1e2430 50%,#5a5a70)"></div>
  <h3>Challenge &amp; Solution</h3>
  <p>A global logistics firm faced challenges with manual data entry and fragmented legacy systems, leading to inefficiencies and human errors.</p>
  <p>Velmora implemented an AI-driven automation platform, integrating disparate systems and streamlining data workflows, reducing operational costs by 30%.</p>
  <a href="#">Read Case Study.....</a>
</article>

<!-- call to action -->
<section class="abs cta" role="img" aria-label="Green-tinted photo of hands working at a laptop"></section>
<h2 class="abs cta-title">Ready to Transform Your IT Strategy?</h2>
<a class="btn btn-fill" style="left:534px;top:2384px;width:131px">Contact Us</a>

<!-- contact -->
<h2 class="abs h2" style="top:2532px;left:-12px">Let’s Get You Back on the Road</h2>
<form>
  <div class="field" style="top:2667px">First Name</div>
  <div class="field" style="top:2732px">Last Name</div>
  <div class="field" style="top:2797px">Email</div>
  <div class="field" style="top:2862px">Message</div>
  <a class="btn btn-fill" style="left:99px;top:2927px;width:131px">Submit</a>
</form>
<div class="abs contact-img" role="img" aria-label="Business person holding a glowing shield with a check mark"></div>

<!-- footer -->
<footer>
  <div class="abs nav" style="top:3066px">
    <div class="brand" style="top:17px"><span class="brand-dot"></span>Velmora Systems GmbH</div>
    <ul class="nav-links">
      <li style="left:376px;top:23px">Home</li>
      <li style="left:465px;top:23px">About</li>
      <li style="left:556px;top:23px">Services<span class="caret">▾</span></li>
      <li style="left:658px;top:23px">Case Studies<span class="caret">▾</span></li>
      <li style="left:784px;top:23px">Contact</li>
    </ul>
    <a class="btn btn-outline" style="left:970px;top:16px;width:130px">Get Started</a>
  </div>
  <div class="abs footer-line" style="top:3147px"></div>
  <p class="abs copy">Copyright © Velmora Systems GmbH.</p>
</footer>

</body>
</html>
```